Marquen Premium Men's Shaving Cream Product Label . Cream packaged in a Amber Jar/Black Top Cap.

Please include information ( see Marquen design Template attachment) designed on a Round Top cap. Label Diameter: 3.125" NOTE: Design this First,
Wrap Around Label: 11.3125 x 0.875" (w x h): NOTE: Required latter after selection of Final Design Selection.
Shave Cream packaged in an 8oz Low Profile Amber Jar/Black Top Cap.
Thanks

Target Market(s)

Prime Target-Men Ages 20yrs-65yrs+ and Women 20yrs-65yrs+( they purchase ovr 55% of these Mens care products for partner/spouse/friend.

Industry/Entity Type

Personel Care/Cosmetics/NaturalHealthcare

Other font styles liked:
• At this stage if you would like to submi a desigh that would include both a Top Label and your Wrap-around label on a Amber jar/black top lid. It would be helpful to see how it would look complete. Thanks . Please refer to the updated design Graphic Template for copy and layout . Questions? Let me know. Thanks.Please now use QUILLSTONE on label designs. Thanks! Please see image attachment for added Tree Image Vector that can be added to your design instead of the Original Tree Image .

Requirements
Must have
• Look and Feel of a Quality/Premium Mens Skincare Brand with a Masculine feel but attractive to women as well ( not Macho!).Think Unisex with a Male slant.
Nice to have
• Premium/Quality/Natural Skincare & Bodycare Brand
Should not have
• Not Macho. No Cartoony or Barber Tools/Bearded Men Images. Too gimicky and over-hyped!

```html
<!DOCTYPE html>
<html lang="en">
<head>
<meta charset="utf-8">
<title>Quillstone Shaving Cream – Lid Label</title>
<link href="https://fonts.googleapis.com/css2?family=Cinzel:wght@400;500;600&display=swap" rel="stylesheet">
<style>
  :root {
    --page: #ffffff;
    --lid-dark: #1b1b1b;
    --lid-mid: #2a2a2a;
    --gold: #c49a5a;
    --ivory: #f4f1ea;
  }
  html, body {
    margin: 0;
    width: 1200px;
    height: 1200px;
    overflow: hidden;
    background: var(--page);
  }
  .lid-label {
    display: block;
    width: 1200px;
    height: 1200px;
  }
  .lid-label text {
    font-family: "Cinzel", serif;
    text-anchor: middle;
  }
  .brand-name { fill: var(--ivory); font-size: 36px; font-weight: 500; letter-spacing: 2px; }
  .product-name { fill: var(--gold); font-size: 84px; font-weight: 500; letter-spacing: 3px; }
  .product-type { fill: var(--ivory); font-size: 39px; font-weight: 500; letter-spacing: 4px; }
  .product-type-fr { fill: var(--ivory); font-size: 28px; font-weight: 500; letter-spacing: 3px; }
  .scent-name { fill: var(--gold); font-size: 26px; font-weight: 500; letter-spacing: 3px; }
  .est-year { fill: var(--ivory); font-size: 20px; letter-spacing: 5px; }
  .net-weight { fill: var(--gold); font-size: 19px; letter-spacing: 1.5px; }
  .rule { stroke: var(--gold); stroke-width: 1.2; }
  .stripe { stroke: var(--gold); stroke-width: 1.4; }
  .ring { fill: none; stroke: var(--gold); }
</style>
</head>
<body>
<svg class="lid-label" viewBox="0 0 1200 1200" xmlns="http://www.w3.org/2000/svg">
  <defs>
    <radialGradient id="lidShade" cx="50%" cy="45%" r="55%">
      <stop offset="0%" stop-color="#2a2a2a"/>
      <stop offset="100%" stop-color="#1b1b1b"/>
    </radialGradient>
    <radialGradient id="emblemTone" cx="50%" cy="50%" r="50%">
      <stop offset="0%" stop-color="#6b5434"/>
      <stop offset="100%" stop-color="#2a241c"/>
    </radialGradient>
    <clipPath id="lidClip"><circle cx="600" cy="600" r="415"/></clipPath>
  </defs>

  <circle class="lid-face" cx="600" cy="600" r="415" fill="url(#lidShade)"/>
  <circle class="ring outer-ring" cx="600" cy="600" r="390" stroke-width="1.2"/>

  <g class="brand">
    <circle cx="600" cy="285" r="8" fill="var(--ivory)"/>
    <text class="brand-name" x="600" y="337">MARQUEN</text>
  </g>

  <text class="product-name" x="600" y="452">QUILLSTONE</text>

  <g class="stripes" clip-path="url(#lidClip)">
    <g class="stripes-left">
      <line class="stripe" x1="180" y1="544" x2="486" y2="544"/>
      <line class="stripe" x1="180" y1="554" x2="486" y2="554"/>
      <line class="stripe" x1="180" y1="564" x2="486" y2="564"/>
      <line class="stripe" x1="180" y1="574" x2="486" y2="574"/>
      <line class="stripe" x1="180" y1="584" x2="486" y2="584"/>
      <line class="stripe" x1="180" y1="594" x2="486" y2="594"/>
      <line class="stripe" x1="180" y1="604" x2="486" y2="604"/>
      <line class="stripe" x1="180" y1="614" x2="486" y2="614"/>
      <line class="stripe" x1="180" y1="624" x2="486" y2="624"/>
      <line class="stripe" x1="180" y1="634" x2="486" y2="634"/>
      <line class="stripe" x1="180" y1="644" x2="486" y2="644"/>
    </g>
    <g class="stripes-right">
      <line class="stripe" x1="734" y1="544" x2="1020" y2="544"/>
      <line class="stripe" x1="734" y1="554" x2="1020" y2="554"/>
      <line class="stripe" x1="734" y1="564" x2="1020" y2="564"/>
      <line class="stripe" x1="734" y1="574" x2="1020" y2="574"/>
      <line class="stripe" x1="734" y1="584" x2="1020" y2="584"/>
      <line class="stripe" x1="734" y1="594" x2="1020" y2="594"/>
      <line class="stripe" x1="734" y1="604" x2="1020" y2="604"/>
      <line class="stripe" x1="734" y1="614" x2="1020" y2="614"/>
      <line class="stripe" x1="734" y1="624" x2="1020" y2="624"/>
      <line class="stripe" x1="734" y1="634" x2="1020" y2="634"/>
      <line class="stripe" x1="734" y1="644" x2="1020" y2="644"/>
    </g>
  </g>

  <g class="emblem">
    <circle class="ring" cx="610" cy="600" r="110" stroke-width="2"/>
    <circle cx="610" cy="600" r="98" fill="url(#emblemTone)" role="img" aria-label="Golden tree of life with spreading roots"/>
    <circle class="ring" cx="610" cy="600" r="98" stroke-width="1"/>
  </g>

  <text class="product-type" x="610" y="772">Shaving Cream</text>
  <text class="product-type-fr" x="610" y="809">Crème de Rasage</text>

  <g class="scent">
    <line class="rule" x1="305" y1="849" x2="434" y2="849"/>
    <text class="scent-name" x="610" y="858">Ashgrove Reserve</text>
    <line class="rule" x1="789" y1="849" x2="918" y2="849"/>
  </g>

  <g class="established">
    <line class="rule" x1="512" y1="890" x2="550" y2="890"/>
    <text class="est-year" x="612" y="897">1935</text>
    <line class="rule" x1="670" y1="890" x2="708" y2="890"/>
  </g>

  <text class="net-weight" x="612" y="961">150g ℮ 5.3 oz</text>
</svg>
</body>
</html>
```